KB Sports & Remedial Massage needs a new logo & business card design

The design is for my Sports and remedial massage business. My business is aimed at everyone who has a muscle ache or injury so not just sports related. I need a design which is sharp, clear and professional. No greens, or pastel colours or floral/girly designs. Perhaps just a Navy background and white text or other way around or perhaps grey. I want to make it clear that I treat everyone and not just sporty people.

Target Market(s)

People with muscle aches or sports injuries

Industry/Entity Type

Health And Wellness

Contact Information for Business Card

It needs to also include the following:
Name: Megan Hartwell
Mobile No: 07493 215 648
Email: meganhartwell@parcelnet.example
Qualifications: Dip SM, Dip SRM

Logo Text

KB Sports & Remedial Massage

Font styles to use
Serif
Other font styles liked:
• Tahoma, Verdana

Colors
5c5c5c
7f7f7f
9d9d9d
0255a3
3176b5
85abd2

Requirements
Must have
• I was thinking of a few simple people figures at the bottom of the card to highlight this i.e. a gardener, musician mixed in with a cyclist and tennis player.
Should not have
• Anything which indicates beauty therapy or relaxing. I am there to get rid of aches and pains and often to give rehab to certain injuries.

```html
<!DOCTYPE html>
<html lang="en">
<head>
<meta charset="utf-8">
<title>KB Sports &amp; Remedial Massage – Business Card</title>
<link rel="stylesheet" href="https://fonts.googleapis.com/css2?family=Open+Sans:wght@400;700&display=swap">
<style>
  :root {
    --stage: #000000;
    --card-front: #d9d9d9;
    --card-back: #ffffff;
    --brand-blue: #0255a3;
    --text-blue: #1a5aa6;
  }
  * { margin: 0; padding: 0; box-sizing: border-box; }
  html, body {
    width: 1200px; height: 900px; overflow: hidden;
    background: var(--stage);
    font-family: "Open Sans", Verdana, sans-serif;
  }
  .canvas { position: relative; width: 1200px; height: 900px; }
  .card {
    position: absolute; top: 271px;
    width: 457px; height: 281px;
    border-radius: 14px;
  }
  .card--front { left: 137px; background: var(--card-front); }
  .card--back { left: 626px; background: var(--card-back); }

  .brand-mark {
    position: absolute; border-radius: 50%;
    background: var(--brand-blue);
  }
  .card--front .brand-mark { left: 41px; top: 68px; width: 145px; height: 145px; }
  .card--back .brand-mark { left: 189px; top: 67px; width: 92px; height: 92px; }

  .brand-name {
    position: absolute; color: var(--brand-blue);
    font-weight: 700; line-height: 1.2;
  }
  .card--front .brand-name { left: 213px; top: 68px; font-size: 16px; }
  .card--back .brand-name {
    left: 0; right: 0; top: 165px; text-align: center; font-size: 19px;
  }

  .holder { position: absolute; left: 213px; top: 122px; color: var(--text-blue); }
  .holder__name { font-size: 18px; font-weight: 400; line-height: 1.2; }
  .holder__quals { font-size: 12px; margin-top: 2px; }

  .contact {
    position: absolute; left: 213px; top: 182px;
    list-style: none; color: var(--text-blue); font-size: 12px;
  }
  .contact li { display: flex; align-items: center; gap: 6px; line-height: 17px; }
  .contact svg { width: 10px; height: 10px; fill: var(--text-blue); }
</style>
</head>
<body>
<main class="canvas">
  <section class="card card--front">
    <div class="brand-mark" role="img" aria-label="Brand emblem"></div>
    <p class="brand-name">KB Sports<br>&amp; Remedial Massage</p>
    <div class="holder">
      <p class="holder__name">Megan Hartwell</p>
      <p class="holder__quals">Dip SM, Dip SRM</p>
    </div>
    <ul class="contact">
      <li>
        <svg viewBox="0 0 10 10" aria-hidden="true"><path d="M2 0.5 L3.6 2.6 L2.8 3.6 Q4 6 6.4 7.2 L7.4 6.4 L9.5 8 L8.4 9.5 Q4.5 9.5 0.5 1.6 Z"/></svg>
        07493 215 648
      </li>
      <li>
        <svg viewBox="0 0 10 10" aria-hidden="true"><path d="M0.5 2 H9.5 V8 H0.5 Z M0.5 2 L5 5.3 L9.5 2" fill="var(--text-blue)"/><path d="M1 2.6 L5 5.5 L9 2.6" stroke="#d9d9d9" stroke-width="0.8" fill="none"/></svg>
        meganhartwell@parcelnet.example
      </li>
    </ul>
  </section>

  <section class="card card--back">
    <div class="brand-mark" role="img" aria-label="Brand emblem"></div>
    <p class="brand-name">KB Sports<br>&amp; Remedial Massage</p>
  </section>
</main>
</body>
</html>
```